Poster Design October

We are a Poker Club (Lakeview Veterans Hall Poker Club). We run poker tournaments three night a week in Mount Gambier
We require a poster to advertise our upcoming major Poker tournament
The details of the event are set out below
ANNUAL $200 BUY IN TOURNAMENT
OCTOBER LONG WEEK END
4-5 OCTOBER 2014
$100K STARTING STACK
45 MIN BLINDS
LAKEVIEW VETERANS HALL
42 KERRIDGE LANE
MOUNT GAMBIER SA 5290
10:00AM START (SA TIME)
REGISTRATION 9:30AM (SA TIME)
EMAIL LVHCARDS@MAILNEST.COM.AU FOR MORE INFORMATION
FIND US ON FRIENDPAGE: LVH CARDS 2014
I have attached a flyer this is something like what we are looking for
I Have also attached the LVH logo which need to be included
Target Market(s)
Poker plyers 18+ both genders
Industry/Entity Type
Club

```html
<!DOCTYPE html>
<html lang="en">
<head>
<meta charset="utf-8">
<title>Lakeview Veterans Hall Poker Club – Annual Tournament</title>
<link rel="stylesheet" href="https://fonts.googleapis.com/css2?family=Arimo:wght@700&family=Gochi+Hand&family=Cinzel:wght@900&family=Lato:wght@700&family=Open+Sans:wght@700&display=swap">
<style>
  :root {
    --stage: #e9e6e2;
    --poster-dark: #1e0c06;
    --poster-mid: #6e2a10;
    --poster-glow: #b4501e;
    --gold: #f6df3c;
    --gold-deep: #f2c52a;
    --white: #ffffff;
    --email: #bfe6f4;
    --strip: #0b0b0b;
    --band: #a3391c;
    --social: #ffffff;
    --social-text: #2f4f8f;
    --badge-edge: #1c1c1c;
    --flame-a: #ffcc33;
    --flame-b: #e9561a;
    --flame-c: #7a1e0a;
  }
  * { margin: 0; padding: 0; box-sizing: border-box; }
  html, body { width: 1200px; height: 900px; overflow: hidden; background: var(--stage); }
  .canvas { position: relative; width: 1200px; height: 900px; }

  .poster {
    position: absolute; left: 343px; top: 27px; width: 559px; height: 848px; overflow: hidden;
    background:
      radial-gradient(ellipse 70% 55% at 50% 45%, var(--poster-glow) 0%, var(--poster-mid) 45%, var(--poster-dark) 100%);
    color: var(--white); text-align: center;
  }
  .line { position: absolute; left: 0; width: 100%; white-space: nowrap; }

  .headline {
    font-family: "Arimo", Arial, sans-serif; font-weight: 700; color: var(--gold);
    text-shadow: 0 2px 3px rgba(0,0,0,.7); letter-spacing: .5px;
  }
  .headline-1 { top: 64px; font-size: 39px; }
  .headline-1 .price { font-size: 47px; }
  .headline-2 { top: 116px; font-size: 39px; }

  .date { font-family: "Gochi Hand", cursive; }
  .date-1 { top: 184px; font-size: 32px; }
  .date-2 { top: 222px; font-size: 28px; }

  .times { font-family: "Cinzel", serif; font-weight: 900; text-shadow: 0 2px 3px rgba(0,0,0,.6); }
  .times .big { font-size: 28px; }
  .times .small { font-size: 19px; }
  .time-1 { top: 282px; }
  .time-2 { top: 318px; }

  .feature { font-family: "Cinzel", serif; font-weight: 900; color: var(--gold-deep); text-shadow: 0 2px 4px rgba(0,0,0,.7); }
  .feature-1 { top: 378px; font-size: 31px; }
  .feature-2 { top: 426px; font-size: 31px; }

  .venue { font-family: "Cinzel", serif; font-weight: 900; font-size: 21px; text-shadow: 0 2px 3px rgba(0,0,0,.7); }
  .venue-1 { top: 492px; }
  .venue-2 { top: 525px; }
  .venue-3 { top: 558px; }

  .email {
    top: 628px; font-family: "Lato", sans-serif; font-weight: 700; font-size: 24px;
    color: var(--email); letter-spacing: 1px; text-shadow: 0 2px 3px rgba(0,0,0,.7);
  }

  .cards-art {
    position: absolute; left: 0; top: 548px; width: 270px; height: 212px;
    background: radial-gradient(ellipse 60% 60% at 40% 60%, var(--flame-a) 0%, var(--flame-b) 45%, rgba(122,30,10,0) 100%);
  }

  .info-strip {
    position: absolute; left: 0; top: 758px; width: 100%; height: 30px; background: var(--strip);
    font-family: "Open Sans", sans-serif; font-weight: 700; font-size: 17px; letter-spacing: .5px;
    text-align: left; padding: 4px 0 0 25px;
  }
  .social-band { position: absolute; left: 0; top: 788px; width: 100%; height: 60px; background: var(--band); }
  .social-name {
    position: absolute; left: 0; top: 0; width: 169px; height: 60px; background: var(--social);
    color: var(--social-text); font-family: "Arimo", Arial, sans-serif; font-weight: 700; font-size: 24px;
    line-height: 60px; text-align: center;
  }
  .social-handle {
    position: absolute; left: 184px; top: 0; line-height: 60px;
    font-family: "Arimo", Arial, sans-serif; font-weight: 700; font-size: 24px; color: var(--white);
  }

  .club-badge { position: absolute; left: 400px; top: 690px; width: 160px; height: 160px; }
  .club-badge .mark {
    font-family: "Arimo", Arial, sans-serif; font-weight: 700; font-size: 30px; fill: var(--band);
  }
</style>
</head>
<body>
<div class="canvas">
  <section class="poster">
    <div class="cards-art" role="img" aria-label="Playing cards engulfed in flames"></div>

    <h1 class="line headline headline-1">ANNUAL <span class="price">$200</span> BUY IN</h1>
    <div class="line headline headline-2">TOURNAMENT</div>

    <p class="line date date-1">OCTOBER LONG WEEK END</p>
    <p class="line date date-2">4-5 OCTOBER 2014</p>

    <p class="line times time-1"><span class="big">10:00AM</span> <span class="small">START (SA TIME)</span></p>
    <p class="line times time-2"><span class="small">REGISTRATION</span> <span class="big">9:30AM</span> <span class="small">(SA TIME)</span></p>

    <p class="line feature feature-1">$100K STARTING STACK</p>
    <p class="line feature feature-2">45 MIN BLINDS</p>

    <address class="venue-block" style="font-style:normal">
      <span class="line venue venue-1">LAKEVIEW VETERANS HALL</span>
      <span class="line venue venue-2">42 KERRIDGE LANE</span>
      <span class="line venue venue-3">MOUNT GAMBIER SA 5290</span>
    </address>

    <p class="line email">EMAIL: LVHCARDS@MAILNEST.COM.AU</p>

    <div class="info-strip">FOR MORE INFORMATION</div>
    <div class="social-band">
      <span class="social-name">FriendPage</span>
      <span class="social-handle">LVH CARDS 2014</span>
    </div>

    <svg class="club-badge" viewBox="0 0 160 160" aria-label="LVH">
      <rect x="30" y="30" width="100" height="100" transform="rotate(45 80 80)" fill="#ffffff" stroke="var(--badge-edge)" stroke-width="4"/>
      <text class="mark" x="80" y="91" text-anchor="middle">LVH</text>
    </svg>
  </section>
</div>
</body>
</html>
```